Willow Frost: CBD and Herbal Topical Pain product needs a brochure

We need a brochure that educates customers on the product. The product combines traditional Chinese herbs used for pain and swelling with a strong dose of CBD to apply topical with a glass, roll-on applicator. We would like to see dark blue as a dominant color or anything ice related. The logo is an iceberg but doesn't need to be included.

Target Market(s)

Cannabis Dispensaries, Chiro, Acu offices,
Health / Wellness, Alternative Medicine

Industry/Entity Type

Alternative Medicine

Colors
0455a3

Requirements
Must have
• Willow Frost
• 500mg CBD in 1oz
• For: Muscle, Joint Pain, Swelling, Acute Injuries, Chronic Pain, Arthritis
• Directions: Apply a thin layer of herbal formula over the affected area. Apply as needed.
• Caution: Avoid hot water shortly after application.
• Ingredients: Angelica Root, Camphor, Cannabidoil (CBD), Cinnamon, Dandelion, Gardenia, Ginger, Licorice, Menthol, Myrrh, Phellodendron Bark, Rhubarb, Safflower, Sesame Oil, Scutellaria
• Highlight amount of CBD: 500mg
• Secondary highlights it includes Turmeric and Magnesium
• Easy Roll-On Topical Pain Relief for Muscle Spasms, Joint Pain, Strains, Sprains, Swelling
• Increases circulation to increase recovery time. Great for athletes
• Stops pain by numbing painful, slower deep nerve signals by stimulating the faster, superficial nerves with a cooling sensation
• Reduce painful swelling and heat involved with inflammation.
• Breaks up damaged tissue to enhance the natural healing process
• Ingredients
• Dang Gui – Angelica : reduces swelling, generates tissue, alleviates pain, expels pus
• Cinnamon –Gui Zhi decreases arthritic pain
• Carthamus Flower / safflower –Hong Hua - reduces swelling, alleviates pain,
• Rhubarb – Da Huang -bruising, acute and chronic swelling
• Licorice –Gan Cao - alleviates spasms, anti-inflammatory
• Phellodendron Huang Bai– reduces swelling and pain
• Dandelion – Pu Gong Ying – reduces swelling and nodules, anti-inflammatory
• Mo Yao – Myrrh – reduces swelling, pain, bruising, and masses, promotes healing
• Ginger – Gan Jiang – chronic swelling, increases circulation
• Gardenia – Zhi Zi- Reduces swelling from trauma, bruising
• Scutellaria – Huang Qin – hot sores, swelling,
• Magnesium – helps muscle spasms
• Camphor – mild, local anesthetic effect, alleviates pain, pain and swelling from sprains
• Menthol – rashes, swelling, relaxes muscles
• Turmeric – reduces inflammation and swelling
• Sesame Oil – carrier oil
• Cannabidiol (CBD) Isolate
• Colloidal Silver (Natural Preservative)
• Formulated by a Herbalist and Doctor of Chinese Medicine, Dr. Dennis Harlow, DAOM
Nice to have
• Iceberg or ice theme
• Copy:
• Willow Frost blends traditional Chinese herbs with a potent dose of hemp derived cannabidiol (CBD) isolate. Instantly feel the cooling icy sensation penetrate deep into sore muscles and joints to sooth away pain.
• Not only does the menthol give a temporary cooling effect which helps numb pain, the other herbal ingredients continue to soothe tight, achy muscles and joints. It can also be applied for an acute sprain or strain to reduce swelling, just like applying ice.
• Ice is used by athletes and recommended by doctors to reduce pain and swelling. Willow Frost can reduce pain and swelling without having to carry a bag of ice around.
• With the easy roll-on application, you dont even have to get your hands cold!
• Traditional Chinese Medicine has used the same herbs for thousands of years to help ease the pain of injuries during battle. Herbal plasters, liniments, and oils were the most common application to maximize the healing benefits of the herbs. Willow Frost uses organic, raw herbs which are ground into a fine powder and further extracted in sesame oil. Once extracted, the oil is filtered and then CBD is then added as the oil is cooling.
• Pictures of a few of the herbs - I have a few already if needed

```html
<!DOCTYPE html>
<html lang="en">
<head>
<meta charset="UTF-8">
<title>Willow Frost Brochure – Inside Spread</title>
<link href="https://fonts.googleapis.com/css2?family=Montserrat:wght@400;500;600;700&display=swap" rel="stylesheet">
<style>
  :root {
    --stage: #e9eaec;
    --navy-deep: #0b2a55;
    --navy: #12407a;
    --brand-blue: #0455a3;
    --orange: #f7a823;
    --white: #ffffff;
    --ice: #dfe9f3;
  }
  html, body {
    margin: 0;
    width: 1200px;
    height: 1200px;
    overflow: hidden;
    background: var(--stage);
    font-family: "Montserrat", Arial, sans-serif;
  }
  .spread {
    position: absolute;
    left: 30px;
    top: 200px;
    width: 1140px;
    height: 800px;
    background: linear-gradient(160deg, var(--navy) 0%, var(--brand-blue) 45%, var(--navy-deep) 100%);
    color: var(--white);
    overflow: hidden;
    box-shadow: 0 10px 30px rgba(0,0,0,0.18);
  }
  .herb-photo {
    position: absolute;
    left: 560px;
    top: 0;
    width: 580px;
    height: 470px;
    background: radial-gradient(ellipse at 55% 45%, rgba(120,140,150,0.55) 0%, rgba(60,80,100,0.35) 45%, rgba(4,40,90,0) 75%);
  }
  .ice-band {
    position: absolute;
    left: 0;
    bottom: 0;
    width: 1140px;
    height: 120px;
    background: linear-gradient(180deg, rgba(223,233,243,0) 0%, rgba(223,233,243,0.55) 55%, var(--ice) 100%);
  }
  .fold-line {
    position: absolute;
    left: 440px;
    top: 0;
    width: 1px;
    height: 64px;
    background: var(--white);
  }
  .accent-line {
    position: absolute;
    left: 440px;
    top: 64px;
    width: 2px;
    height: 640px;
    background: var(--orange);
  }
  .panel { position: absolute; top: 0; height: 100%; box-sizing: border-box; }
  .panel-info { left: 0; width: 440px; padding: 60px 34px 0 40px; }
  .panel-ingredients { left: 440px; width: 700px; padding: 44px 40px 0 36px; }
  .pill {
    display: inline-block;
    background: var(--orange);
    color: var(--white);
    font-weight: 700;
    font-size: 18px;
    letter-spacing: 1.5px;
    text-transform: uppercase;
    padding: 6px 20px;
    border-radius: 20px;
  }
  .dose {
    font-size: 26px;
    font-weight: 700;
    margin: 14px 0 12px;
  }
  .hl { color: var(--orange); }
  .spec {
    font-size: 13.5px;
    line-height: 1.5;
    margin: 0 0 8px;
    letter-spacing: 0.3px;
  }
  .spec .label { color: var(--orange); font-weight: 700; }
  .highlight {
    font-size: 17px;
    font-weight: 700;
    margin: 18px 0 4px;
  }
  .secondary {
    font-size: 15px;
    font-weight: 700;
    color: var(--orange);
    margin: 0 0 8px;
  }
  .benefits, .ingredient-list {
    list-style: none;
    margin: 0;
    padding: 0;
  }
  .benefits li, .ingredient-list li {
    position: relative;
    padding-left: 14px;
    font-size: 13.5px;
    line-height: 1.5;
    letter-spacing: 0.3px;
  }
  .benefits li::before, .ingredient-list li::before {
    content: "";
    position: absolute;
    left: 0;
    top: 8px;
    width: 5px;
    height: 5px;
    border-radius: 50%;
    background: var(--orange);
  }
  .ingredient-list { margin-top: 16px; }
  .ingredient-list li { font-size: 14px; line-height: 1.68; }
  .credit {
    margin-top: 14px;
    font-size: 14px;
    font-weight: 600;
    color: var(--orange);
  }
</style>
</head>
<body>
  <main class="spread">
    <div class="herb-photo" role="img" aria-label="Photo of glass jars holding dried Chinese herbs, powders and leaves on a dark blue wooden surface"></div>
    <div class="ice-band" role="img" aria-label="Icy white crystals along the bottom edge"></div>
    <div class="fold-line"></div>
    <div class="accent-line"></div>

    <section class="panel panel-info">
      <span class="pill">Willow Frost</span>
      <p class="dose"><span class="hl">500mg</span> CBD in 1oz</p>
      <p class="spec"><span class="label">For:</span> Muscle, Joint Pain, Swelling, Acute Injuries, Chronic Pain, Arthritis</p>
      <p class="spec"><span class="label">Directions:</span> Apply a thin layer of herbal formula over the affected area. Apply as needed.</p>
      <p class="spec"><span class="label">Caution:</span> Avoid hot water shortly after application.</p>
      <p class="spec"><span class="label">Ingredients:</span> Angelica Root, Camphor, Cannabidoil (CBD), Cinnamon, Dandelion, Gardenia, Ginger, Licorice, Menthol, Myrrh, Phellodendron Bark, Rhubarb, Safflower, Sesame Oil, Scutellaria</p>
      <p class="highlight">Highlight amount of CBD: <span class="hl">500mg</span></p>
      <p class="secondary">Secondary highlights it includes Turmeric and Magnesium</p>
      <ul class="benefits">
        <li>Easy Roll-On Topical Pain Relief for Muscle Spasms, Joint Pain, Strains, Sprains, Swelling</li>
        <li>Increases circulation to increase recovery time. Great for athletes</li>
        <li>Stops pain by numbing painful, slower deep nerve signals by stimulating the faster, superficial nerves with a cooling sensation</li>
        <li>Reduce painful swelling and heat involved with inflammation</li>
        <li>Breaks up damaged tissue to enhance the natural healing process.</li>
      </ul>
    </section>

    <section class="panel panel-ingredients">
      <span class="pill">Ingredients</span>
      <ul class="ingredient-list">
        <li>Dang Gui – Angelica : reduces swelling, generates tissue, alleviates pain, expels pus</li>
        <li>Cinnamon – Gui Zhi decreases arthritic pain</li>
        <li>Carthamus Flower / safflower – Hong Hua - reduces swelling, alleviates pain</li>
        <li>Licorice – Gan Cao - alleviates spasms, anti-inflammatory</li>
        <li>Phellodendron Huang Bai – reduces swelling and pain</li>
        <li>Dandelion – Pu Gong Ying – reduces swelling and nodules, anti-inflammatory</li>
        <li>Mo Yao – Myrrh – reduces swelling, pain, bruising, and masses, promotes healing</li>
        <li>Ginger – Gan Jiang – chronic swelling, increases circulation</li>
        <li>Gardenia – Zhi Zi - Reduces swelling from trauma, bruising</li>
        <li>Scutellaria – Huang Qin – hot sores, swelling</li>
        <li>Magnesium – helps muscle spasms</li>
        <li>Camphor – mild, local anesthetic effect, alleviates pain, pain and swelling from sprains</li>
        <li>Menthol – rashes, swelling, relaxes muscles</li>
        <li>Turmeric – reduces inflammation and swelling</li>
        <li>Sesame Oil – carrier oil</li>
        <li>Cannabidiol (CBD) Isolate</li>
        <li>Colloidal Silver (Natural Preservative)</li>
      </ul>
      <p class="credit">Formulated by a Herbalist and Doctor of Chinese Medicine, Dr. Dennis Harlow, DAOM</p>
    </section>
  </main>
</body>
</html>
```